Restaurant Finder Website Design

I need to create a website that will help people find restaurants around a zip code or address.

I would like to have a very clean and simple design. I will need a design for the homepage, that should be very clean and simple to use. its where the users will launch their search. I am thinking something like tavlex like.. big search field with a very clean page where users can create an account or restaurants subscribe to the service.

Also need the design of the search results page, I would like to display a big map with the results and a list on the side or the bottom of the map.

Also need a profile page for the users that sign up to the site.

Mostly what I need are guidelines and color coordinated elements, like a general layout and buttons that work together. I would like to know what the action buttons and elements should look like. Because its going to have some more detail pages.

Target Market(s)

People in general, mainly people that work at an office and have to find a place for lunch every day.

Industry/Entity Type

Restaurant

Number of Pages Required

4 page

Font styles to use
Serif
Sans Serif

Requirements
Must have
• It must be a really simple and clean design but look edgy.

```html
<!DOCTYPE html>
<html lang="en">
<head>
<meta charset="utf-8">
<title>LunchNear – My Dashboard</title>
<link rel="stylesheet" href="https://fonts.googleapis.com/css2?family=Lato:wght@400;700&family=Raleway:wght@400;500;600;700&family=Courgette&display=swap">
<style>
:root{
  --red:#d10d0d;
  --ink:#2a2a2a;
  --text:#444;
  --muted:#8a8a8a;
  --line:#dcdcdc;
  --panel:#efefef;
  --navy:#1f2a38;
  --black:#0b0b0b;
}
*{box-sizing:border-box;margin:0;padding:0}
html,body{width:1200px;height:889px;overflow:hidden;background:#fff}
body{position:relative;font-family:"Raleway",sans-serif;color:var(--text)}
.abs{position:absolute}

/* header */
.site-header{position:absolute;left:0;top:0;width:1200px;height:76px;background:linear-gradient(#fff,#efefef);border-bottom:2px solid var(--red)}
.brand{position:absolute;left:162px;top:20px;display:flex;align-items:center;gap:10px;font-family:"Raleway",sans-serif;font-weight:600;font-size:26px;color:var(--ink)}
.brand-dot{width:30px;height:30px;border-radius:50%;background:var(--red)}
.search{position:absolute;left:430px;top:18px;width:353px;height:39px;border:1px solid #ccc;background:#fff;font-size:12px;color:#999;padding:11px 13px}
.search svg{position:absolute;right:11px;top:11px}
.btn{position:absolute;top:21px;height:32px;color:#fff;font-weight:700;font-size:11px;display:flex;align-items:center;justify-content:center}
.btn-login{left:854px;width:81px;background:var(--navy)}
.btn-register{left:943px;width:96px;background:var(--red)}

/* sidebar */
.sidebar{position:absolute;left:162px;top:118px;width:210px;height:616px;border:1px solid var(--line)}
.profile{height:138px;border-bottom:2px solid var(--ink);text-align:center}
.avatar{position:absolute;left:65px;top:15px;width:78px;height:78px;border-radius:50%;border:3px solid var(--red);background:linear-gradient(#e3e3e3,#cfcfcf)}
.profile-name{position:absolute;left:0;width:208px;top:103px;font-family:"Lato",sans-serif;font-weight:700;font-size:14px;color:var(--ink)}
.menu{list-style:none}
.menu li{height:39.8px;border-bottom:1px solid var(--line);padding-left:24px;display:flex;align-items:center;font-weight:700;font-size:10.4px;color:var(--ink);position:relative}
.menu li:last-child{border-bottom:0}
.menu li::before{content:"";position:absolute;left:15px;top:17px;border-left:3.5px solid #555;border-top:3px solid transparent;border-bottom:3px solid transparent}
.menu li.active{color:var(--red)}
.menu li.active::before{border-left-color:var(--red)}

/* main */
.page-title{left:394px;top:116px;font-family:"Lato",sans-serif;font-weight:700;font-size:17.5px;color:var(--ink)}
.rule{position:absolute;left:394px;width:645px;height:1px;background:var(--line)}
.hello{left:395px;top:165px;font-family:"Lato",sans-serif;font-weight:700;font-size:12.5px;color:var(--ink)}
.hello span{color:var(--red)}
.intro{left:395px;top:186px;width:645px;font-size:11.3px;line-height:17px}
.section-title{display:flex;align-items:center;gap:9px;font-family:"Lato",sans-serif;font-weight:700;font-size:15.5px;color:var(--ink)}
.card{position:absolute;width:311px;border:1px solid var(--line)}
.card-head{height:30px;background:var(--panel);display:flex;align-items:center;gap:8px;padding-left:16px;font-family:"Lato",sans-serif;font-weight:700;font-size:13.5px;color:var(--ink)}
.row{height:42px;border-top:1px solid var(--line);display:flex;align-items:center;padding-left:16px;gap:8px;font-size:11.3px;position:relative}
.row:first-of-type{border-top:0}
.edit{position:absolute;right:14px;font-size:11.3px;color:var(--red);display:flex;align-items:center;gap:4px}
.addr{padding:15px 18px 0;font-size:11.3px;line-height:17px}
.addr strong{display:block;font-family:"Lato",sans-serif;font-size:13px;color:var(--ink);margin-bottom:3px}

/* footer */
.footer-band{position:absolute;left:0;top:778px;width:1200px;height:75px;background:var(--red);color:#fff}
.footer-links{position:absolute;left:163px;top:15px;font-family:"Lato",sans-serif;font-weight:700;font-size:11.5px}
.footer-links span{margin:0 6px}
.follow{position:absolute;left:163px;top:48px;display:flex;align-items:center;gap:6px;font-family:"Courgette",cursive;font-size:15px}
.follow i{width:21px;height:21px;border-radius:50%;background:#fff;display:inline-block;margin-left:2px}
.footer-brand{position:absolute;left:838px;top:18px;display:flex;align-items:center;gap:10px;font-family:"Raleway",sans-serif;font-weight:600;font-size:26px}
.footer-brand .brand-dot{background:#fff;width:32px;height:32px}
.bottom-bar{position:absolute;left:0;top:853px;width:1200px;height:36px;background:var(--black);color:#ddd;font-family:"Lato",sans-serif;font-size:11px}
.bottom-bar .copy{position:absolute;left:162px;top:11px}
.bottom-bar .legal{position:absolute;right:161px;top:11px}
.bottom-bar .legal span{border-left:1px solid #555;margin-left:14px;padding-left:14px}
</style>
</head>
<body>

<header class="site-header">
  <div class="brand"><span class="brand-dot"></span>LunchNear</div>
  <div class="search">Zip Code or Address
    <svg width="15" height="15" viewBox="0 0 16 16"><circle cx="6.5" cy="6.5" r="5" fill="none" stroke="#999" stroke-width="2"/><line x1="10.3" y1="10.3" x2="15" y2="15" stroke="#999" stroke-width="2.4"/></svg>
  </div>
  <div class="btn btn-login">LOGIN</div>
  <div class="btn btn-register">REGISTER</div>
</header>

<aside class="sidebar">
  <div class="profile">
    <div class="avatar" role="img" aria-label="User profile picture placeholder"></div>
    <div class="profile-name">Mr. Alan Brightwell</div>
  </div>
  <ul class="menu">
    <li class="active">ACCOUNT DASHBOARD</li>
    <li>ACCOUNT INFORMATION</li>
    <li>ADDRESS BOOK</li>
    <li>MY ORDERS</li>
    <li>BILLING AGREEMENTS</li>
    <li>RECURRING PROFILES</li>
    <li>MY PRODUCT REVIEWS</li>
    <li>MY TAGS</li>
    <li>WISHLIST</li>
    <li>MY APPLICATIONS</li>
    <li>NEWSLETTER SUBSCRIPTIONS</li>
    <li>MY DOWNLOADABLE PRODUCTS</li>
  </ul>
</aside>

<main>
  <h1 class="abs page-title">My Dashboard</h1>
  <div class="rule" style="top:149px"></div>
  <p class="abs hello">Hello, <span>Lunch Near</span></p>
  <p class="abs intro">From your My Account Dashboard you have the ability to view a snapshot of your recent account activity and update your account information. Select a link below to view or edit information.</p>

  <h2 class="abs section-title" style="left:394px;top:241px">
    <svg width="21" height="17" viewBox="0 0 21 17"><path d="M0 2h7l2 2h12v13H0z" fill="var(--red)"/><circle cx="11" cy="9" r="2.3" fill="#fff"/><path d="M7 15c0-3 8-3 8 0z" fill="#fff"/></svg>
    Account Information</h2>
  <div class="rule" style="top:273px"></div>

  <section class="card" style="left:394px;top:290px;height:156px">
    <div class="card-head">
      <svg width="16" height="15" viewBox="0 0 16 15"><path d="M1 5c0-4 14-4 14 0l-3 1-1-2H5L4 6z" fill="var(--red)"/><rect x="3" y="6" width="10" height="8" rx="2" fill="var(--red)"/><circle cx="8" cy="10" r="2" fill="#fff"/></svg>
      Contact Information</div>
    <div class="row"><svg width="9" height="10" viewBox="0 0 9 10"><circle cx="4.5" cy="3" r="2.6" fill="#999"/><path d="M0 10c0-5 9-5 9 0z" fill="#999"/></svg>Lunch Near</div>
    <div class="row"><svg width="10" height="8" viewBox="0 0 10 8"><rect width="10" height="8" fill="#999"/><path d="M0 0l5 4 5-4" fill="none" stroke="#fff"/></svg>hello@lunchnear.com &nbsp;- Change Email</div>
    <div class="row"><svg width="10" height="10"><circle cx="5" cy="5" r="5" fill="#999"/></svg>Change Password
      <span class="edit"><svg width="11" height="10" viewBox="0 0 11 10"><rect x="0.5" y="1.5" width="8" height="8" fill="none" stroke="var(--red)"/><path d="M4 6l6-6" stroke="var(--red)" stroke-width="1.6"/></svg>Edit</span></div>
  </section>

  <section class="card" style="left:728px;top:290px;height:156px">
    <div class="card-head">
      <svg width="16" height="14" viewBox="0 0 16 14"><path d="M0 5l8-5 8 5v9H0z" fill="var(--red)"/><rect x="3" y="3" width="10" height="5" fill="#fff"/></svg>
      Newsletters</div>
    <p style="padding:13px 16px;font-size:11.3px">You are currently subscribed to 'General Subscription'.</p>
    <span class="edit" style="top:131px"><svg width="11" height="10" viewBox="0 0 11 10"><rect x="0.5" y="1.5" width="8" height="8" fill="none" stroke="var(--red)"/><path d="M4 6l6-6" stroke="var(--red)" stroke-width="1.6"/></svg>Edit</span>
  </section>

  <h2 class="abs section-title" style="left:394px;top:474px">
    <svg width="14" height="17" viewBox="0 0 14 17"><rect x="1" y="1" width="12" height="15" rx="2" fill="none" stroke="var(--red)" stroke-width="2"/><circle cx="7" cy="7" r="2" fill="var(--red)"/><path d="M3.5 13c0-3 7-3 7 0z" fill="var(--red)"/></svg>
    Address Book</h2>
  <span class="abs" style="right:161px;top:478px;font-size:11px;color:var(--text)">Manage Addresses</span>
  <div class="rule" style="top:505px"></div>

  <section class="card" style="left:394px;top:523px;height:170px">
    <div class="card-head" style="gap:11px">
      <svg width="12" height="15" viewBox="0 0 12 15"><rect x="1" y="1" width="10" height="13" fill="none" stroke="var(--red)" stroke-width="1.8"/><path d="M3 5h6M3 8h6M3 11h4" stroke="var(--red)" stroke-width="1.3"/></svg>
      Billing Details</div>
    <div class="addr"><strong>Lunch Near</strong>123, Milano Tower, Near Nibh Nonumy,<br>Consequtw, Gohnbrg - 123456<br>Dollortado<br>MORFXD</div>
    <span class="edit" style="top:146px;right:9px"><svg width="11" height="10" viewBox="0 0 11 10"><rect x="0.5" y="1.5" width="8" height="8" fill="none" stroke="var(--red)"/><path d="M4 6l6-6" stroke="var(--red)" stroke-width="1.6"/></svg>Edit address</span>
  </section>

  <section class="card" style="left:728px;top:523px;height:170px">
    <div class="card-head" style="padding-left:17px;gap:10px">
      <svg width="19" height="15" viewBox="0 0 19 15"><rect x="6" y="0" width="9" height="8" fill="var(--red)"/><path d="M0 9h5l4 2h6l3-2v3l-5 3H5L0 13z" fill="var(--red)"/></svg>
      Shipping Details</div>
    <div class="addr" style="padding-left:16px"><strong>Lunch Near</strong>123, Milano Tower, Near Nibh Nonumy,<br>Consequtw, Gohnbrg - 123456<br>Dollortado<br>MORFXD</div>
    <span class="edit" style="top:146px;right:6px"><svg width="11" height="10" viewBox="0 0 11 10"><rect x="0.5" y="1.5" width="8" height="8" fill="none" stroke="var(--red)"/><path d="M4 6l6-6" stroke="var(--red)" stroke-width="1.6"/></svg>Edit address</span>
  </section>
</main>

<footer>
  <div class="footer-band">
    <nav class="footer-links">Home<span>|</span>What's This?<span>|</span>Dish<span>|</span>Places<span>|</span>Blog<span>|</span>Contact Us</nav>
    <div class="follow">Follow Us :<i></i><i></i><i></i></div>
    <div class="footer-brand"><span class="brand-dot"></span>LunchNear</div>
  </div>
  <div class="bottom-bar">
    <span class="copy">© Copyright 2016 &nbsp;Lunch Near. &nbsp;| All Rights Reserved</span>
    <span class="legal">Terms Of Use<span>Privacy Statements</span></span>
  </div>
</footer>

</body>
</html>
```